VALMORE INDUSTRIES est une société dont l'activité est orienté INDUSTRIE TECHNIQUE. Notre activité...

Ce flyer d‘une page doit décrire les principaux thèmes de nos activités
Il faut donc faire mentionner sur le flyer :
- LA FORMATION pompes, ATEX, robinetterie...
-Actualités industrielles ROUAGES D'USINE
-Le magazine VALMORE BREF HEBDO
- ATELIER OPTIMAL expertise, conseil...
Egalement écrire sur le flyer la phrase suivante :
VALMORE Industries vous présente son savoir faire
ainsi que notre adresse mail www.valmoreindustries-exemple.fr
et notre téléphone +33 (1) 55 20 61 39
Et bien sur ajouter notre logo qui est en pièce jointe
Ce flyer sera essentiellement distribué lors de grands salons d'expositions à nos clients et futurs clients. il sera également adressé par voie postale à nos lecteurs soit environ 15000 exemplaires
En vous remerciant par avance

```html
<!DOCTYPE html>
<html lang="fr">
<head>
<meta charset="utf-8">
<title>VALMORE INDUSTRIES – Flyer</title>
<link rel="stylesheet" href="https://fonts.googleapis.com/css2?family=PT+Sans:ital,wght@0,400;0,700;1,400;1,700&display=swap">
<style>
  :root {
    --page-bg: #dcdcdc;
    --paper: #ffffff;
    --ink: #111111;
    --green: #4cb848;
    --green-light: #8dc63f;
    --green-dark: #2f8f3a;
    --grey-bar: #b9b9b9;
    --blue-bar: #00aeef;
    --orange-bar: #f7941d;
    --dark-1: #5a5a5a;
    --dark-2: #151515;
    --white: #ffffff;
  }
  * { margin: 0; padding: 0; box-sizing: border-box; }
  html, body {
    width: 1200px; height: 960px; overflow: hidden;
    background: var(--page-bg);
    font-family: "PT Sans", sans-serif;
  }
  .stage { position: relative; width: 1200px; height: 960px; }
  .flyer {
    position: absolute; left: 284px; top: 30px;
    width: 520px; height: 740px;
    transform: scale(1.2162); transform-origin: 0 0;
    background: var(--paper);
    box-shadow: 0 4px 14px rgba(0,0,0,.18);
    overflow: hidden;
  }
  .shapes, .photo { position: absolute; left: 0; top: 0; width: 520px; height: 740px; }
  .brand-title {
    position: absolute; left: 24px; top: 28px;
    font-weight: 700; font-size: 24px; color: var(--ink); letter-spacing: -.2px;
  }
  .brand-mail {
    position: absolute; left: 33px; top: 57px;
    font-weight: 700; font-size: 16px; color: var(--ink);
  }
  .logo {
    position: absolute; display: flex; align-items: center; gap: 6px;
    font-weight: 700; font-size: 17px; color: var(--green-dark); letter-spacing: .5px;
  }
  .logo .dot { width: 16px; height: 16px; border-radius: 50%; background: var(--green); }
  .logo--header { left: 392px; top: 42px; }
  .logo--footer { left: 380px; top: 680px; color: var(--white); }
  .logo--footer .dot { background: var(--white); }
  .headline {
    position: absolute; left: 10px; top: 140px; width: 260px;
    text-align: center; color: var(--white);
    font-style: italic; font-size: 26px; line-height: 35px;
    text-shadow: 2px 3px 4px rgba(0,0,0,.85);
  }
  .services-tab {
    position: absolute; left: 24px; top: 339px;
    font-weight: 700; font-size: 20px; color: var(--ink);
    text-shadow: 0 0 2px #fff;
  }
  .service {
    position: absolute; left: 20px; display: flex; align-items: center; gap: 6px;
    font-size: 17px; color: var(--ink);
  }
  .service svg { flex: none; }
  .service--formations { top: 405px; font-size: 18px; }
  .service--regie { top: 466px; font-weight: 700; font-size: 16px; }
  .service--revue { top: 524px; font-weight: 700; font-size: 16px; }
  .service--rouages { top: 582px; font-weight: 700; font-size: 16px; }
  .about-title {
    position: absolute; left: 238px; top: 354px; width: 282px; text-align: center;
    color: var(--white); font-style: italic; font-size: 19px;
  }
  .about-text {
    position: absolute; left: 250px; top: 386px; width: 266px;
    color: var(--white); font-style: italic; font-weight: 700; font-size: 11px; line-height: 16.4px;
  }
  .about-text .line { display: block; white-space: nowrap; }
  .address {
    position: absolute; left: 58px; top: 658px;
    font-weight: 700; font-size: 13.5px; line-height: 18px; color: var(--ink);
  }
  .phone {
    position: absolute; left: 66px; top: 704px;
    font-weight: 700; font-size: 13.5px; color: var(--ink);
  }
</style>
</head>
<body>
<main class="stage">
  <article class="flyer">
    <svg class="shapes" viewBox="0 0 520 740" aria-hidden="true">
      <defs>
        <linearGradient id="dark-panel" x1="0" y1="0" x2="1" y2="1">
          <stop offset="0" stop-color="var(--dark-1)"/>
          <stop offset=".7" stop-color="var(--dark-2)"/>
        </linearGradient>
        <linearGradient id="about-panel" x1="0" y1="0" x2="0" y2="1">
          <stop offset="0" stop-color="#222"/>
          <stop offset=".5" stop-color="#4a4a4a"/>
          <stop offset="1" stop-color="#1a1a1a"/>
        </linearGradient>
        <linearGradient id="footer-band" x1="0" y1="0" x2="1" y2="0">
          <stop offset="0" stop-color="var(--green)"/>
          <stop offset=".45" stop-color="var(--green-light)"/>
          <stop offset=".55" stop-color="#a8d65a"/>
          <stop offset="1" stop-color="var(--green)"/>
        </linearGradient>
        <filter id="bar-shadow" x="-5%" y="-10%" width="115%" height="140%">
          <feDropShadow dx="2" dy="2" stdDeviation="1.5" flood-opacity=".45"/>
        </filter>
      </defs>
      <polygon points="0,85 282,85 240,318 0,318" fill="url(#dark-panel)"/>
      <polygon points="282,85 298,85 256,318 240,318" fill="var(--green)"/>
      <polygon points="238,318 520,318 520,331 236,331" fill="var(--green)"/>
      <polygon points="238,331 520,331 520,645 280,645" fill="url(#about-panel)"/>
      <rect x="0" y="330" width="182" height="47" fill="var(--green)" filter="url(#bar-shadow)"/>
      <rect x="0" y="393" width="217" height="56" fill="var(--green)" filter="url(#bar-shadow)"/>
      <rect x="0" y="453" width="239" height="55" fill="var(--grey-bar)" filter="url(#bar-shadow)"/>
      <rect x="0" y="514" width="251" height="49" fill="var(--blue-bar)" filter="url(#bar-shadow)"/>
      <rect x="0" y="570" width="257" height="45" fill="var(--orange-bar)" filter="url(#bar-shadow)"/>
      <rect x="0" y="645" width="520" height="95" fill="url(#footer-band)"/>
      <path d="M20 672 L35 659 L50 672 L46 672 L46 684 L38 684 L38 677 L32 677 L32 684 L24 684 L24 672 Z" fill="#8a8a8a"/>
      <path d="M22 703 Q35 696 48 703 L46 708 L41 707 L40 704 Q35 702 30 704 L29 707 L24 708 Z M27 709 L43 709 L46 718 L24 718 Z" fill="#8a8a8a"/>
    </svg>

    <svg class="photo" viewBox="0 0 520 740" role="img" aria-label="Photo de pipelines industriels devant une raffinerie dans la brume">
      <defs>
        <linearGradient id="photo-tone" x1="0" y1="0" x2="0" y2="1">
          <stop offset="0" stop-color="#c9c3b3"/>
          <stop offset=".45" stop-color="#a39d8a"/>
          <stop offset="1" stop-color="#4f4c42"/>
        </linearGradient>
      </defs>
      <polygon points="298,85 520,85 520,318 256,318" fill="url(#photo-tone)"/>
    </svg>

    <h1 class="brand-title">VALMORE INDUSTRIES</h1>
    <p class="brand-mail">contact@valmoreindustries-exemple.fr</p>
    <div class="logo logo--header"><span class="dot"></span>VALMORE</div>

    <h2 class="headline">VALMORE Industries<br>vous présente<br>son savoir faire</h2>

    <h3 class="services-tab">NOS SERVICES</h3>
    <div class="service service--formations">
      <svg width="26" height="26" viewBox="0 0 26 26" aria-hidden="true"><path d="M6 3 L21 5 L19 23 L4 21 Z" fill="#fff" stroke="#111" stroke-width="1.6"/></svg>
      Nos formations
    </div>
    <div class="service service--regie">
      <svg width="30" height="24" viewBox="0 0 30 24" aria-hidden="true"><path d="M3 9 L10 9 L20 3 L20 21 L10 15 L3 15 Z M8 15 L10 22" fill="none" stroke="#111" stroke-width="1.6"/><path d="M23 8 Q26 12 23 16" fill="none" stroke="#111" stroke-width="1.6"/></svg>
      Notre régie publicitaire
    </div>
    <div class="service service--revue">
      <svg width="24" height="30" viewBox="0 0 24 30" aria-hidden="true"><rect x="4" y="3" width="17" height="24" fill="#fff" stroke="#111" stroke-width="1.5"/><path d="M2 6h4M2 10h4M2 14h4M2 18h4M2 22h4" stroke="#111" stroke-width="1.3"/></svg>
      Notre revue: Bref Hebdo
    </div>
    <div class="service service--rouages">
      <svg width="36" height="26" viewBox="0 0 36 26" aria-hidden="true"><rect x="2" y="2" width="32" height="18" fill="none" stroke="#111" stroke-width="1.8"/><path d="M14 24 h8 M18 20 v4" stroke="#111" stroke-width="1.8"/></svg>
      Rouages d'usine
    </div>

    <h3 class="about-title">QUI SOMMES NOUS?</h3>
    <div class="about-text">
      <span class="line" style="margin-left:0">Leader depuis plus de 25 ans dans le domaine</span>
      <span class="line" style="margin-left:4px">de la formation technique VALMORE Industries</span>
      <span class="line" style="margin-left:7px">forme les personnels des industries</span>
      <span class="line" style="margin-left:9px">de process et ceux des secteurs</span>
      <span class="line" style="margin-left:12px">eau-environnement-énergie.</span>
      <span class="line" style="margin-left:12px">C'est également un département d'édition,</span>
      <span class="line" style="margin-left:14px">une régie publicitaire présente</span>
      <span class="line" style="margin-left:17px">sur 6 supports, un service de formation et</span>
      <span class="line" style="margin-left:21px">d'information technique sur le web,</span>
      <span class="line" style="margin-left:24px">et le conseil expert ATELIER OPTIMAL.</span>
    </div>

    <p class="address">Avenue des Tilleuls 42<br>Villebrune-sur-Marne 94500-F</p>
    <p class="phone">+33 (1) 55 20 61 39</p>
    <div class="logo logo--footer"><span class="dot"></span>VALMORE</div>
  </article>
</main>
</body>
</html>
```